Flyer-Design für Dienstleister für 3D-Druck Produkte
Zielgruppe
Ich fungiere als Dienstleister für 3D-Druck Produkte. Ich besitze einen 3D-Vollfarbdrucker, den es auf dem Markt nur sehr selten gibt. Mit den diversen Alleinstellungsmerkmalen die dieser 3D-Drucker hat, können die unterschiedlichsten Zielgruppen bzw. Branchen (Anwendungsbeispiele: Prototypen, Prothesen, Spielzeug, Kleinserien, Funktionsmodelle, Architekturmodelle, Modellbau, Präsentationen, Beschriftungen, etc.) angesprochen werden.
Dieser Flyer soll hauptsächlich um den 3D-Vollfarbdruck drehen. Dieser soll dann später zu Werbezwecken dienen
Zielgruppen:
-Firmen,
-Konstruktionsbüro,
-Labore
-Architekturbüros
-Designer
-Forschungseinrichtungen
-Hochschulen und Studenten
Aufgabenstellung
Ich möchte gern diese Vielfalt und die Vorteile auf einen Flyer im Format Din Lang bringen. Dieser sollte so 6 oder 8 Seiten besitzen, je nach Platz und Gestaltung. Der Flyer soll hochwertig und modern aussehen - klar im Design, aber trotzdem ansprechend-inspirierend. Dazwischen als eleganter Eyecatcher einige Produktfotos. Es sollte aber keinesfalls überfrachtet sein.
Das Farbdesign sollte sich an meine Webseite anlehnen, auch die nötigen Informationen können von dieser Seite entnommen werden. Weitere Fotos von den gedruckten Bauteilen sende ich Ihnen zu. Falls Sie kreative Fotoideen haben, dann können Sie mir auch jederzeit schreiben und ich versuche diese so gut wie möglich umzusetzen.
Landingpage: https://formwerkstatt-plus.de/3d-vollfarbdruck/
Hier stehen sämtliche Informationen zur Verfügung.

```html
<!DOCTYPE html>
<html lang="de">
<head>
<meta charset="utf-8">
<title>formwerkstatt – Flyer 3D-Vollfarbdruck</title>
<link href="https://fonts.googleapis.com/css2?family=Poppins:ital,wght@0,400;0,500;0,600;1,400&family=Open+Sans:wght@400;600&display=swap" rel="stylesheet">
<style>
:root{
  --stage:#3a3a3a;
  --paper:#ffffff;
  --teal:#149b93;
  --teal-dark:#0f7f78;
  --ink:#1f1f1f;
  --body:#4a4a4a;
  --tint:#e7f3f4;
  --lavender:#e6e5f0;
}
*{margin:0;padding:0;box-sizing:border-box}
html,body{width:1200px;height:3335px;overflow:hidden;background:var(--stage)}
body{font-family:"Open Sans",Arial,sans-serif;color:var(--body)}
.spread{position:absolute;left:50px;width:1100px;height:784px;background:var(--paper);overflow:hidden}
.spread--outside{top:790px}
.spread--inside{top:1770px}
.shape{position:absolute;display:block}
.abs{position:absolute}
h2{font-family:"Poppins",Arial,sans-serif;font-weight:500;color:var(--ink);font-size:24px;line-height:1.15}
.sub{font-family:"Poppins",Arial,sans-serif;font-size:9px;color:var(--ink);margin-top:1px}
.wave{display:block;width:34px;height:8px;margin-top:8px}
.body{font-size:9.2px;line-height:1.68}
.body p{margin-bottom:12px}
.body b{color:var(--teal);font-weight:600}
.center{text-align:center}
.panel-why{left:48px;top:88px;width:300px}
.panel-why .body{margin-top:22px}
.panel-contact{left:395px;top:84px;width:300px}
.panel-contact .wave{margin:8px auto 0}
.panel-contact .intro{margin-top:20px;font-size:9.2px;line-height:1.6}
.contact{margin-top:16px;font-size:9.2px;line-height:1.7}
.contact strong{font-family:"Poppins",Arial,sans-serif;font-weight:500;font-size:12px;color:var(--ink);display:block}
.contact a{color:var(--teal);text-decoration:none}
.panel-cover{left:770px;top:497px;width:300px}
.panel-cover h2{font-size:24px}
.panel-cover .wave{margin:8px auto 0}
.panel-cover .lead{margin-top:22px;font-size:11px;line-height:1.55}
.panel-cover .cta{margin-top:16px;font-size:11px;color:var(--teal)}
.brand{display:flex;align-items:center;justify-content:center;gap:8px;margin-top:46px;font-family:"Poppins",Arial,sans-serif;font-weight:600;font-size:22px;color:var(--teal)}
.brand i{display:block;width:14px;height:14px;background:var(--teal)}
.panel-process{left:48px;top:324px;width:300px}
.panel-process .body{margin-top:20px;font-size:8.6px}
.uses-title{font-family:"Poppins",Arial,sans-serif;font-weight:600;color:var(--teal);font-size:9.5px;margin-top:2px}
.uses{list-style:none;margin-top:8px}
.uses li{display:flex;align-items:center;gap:7px;font-size:9px;line-height:18px}
.uses svg{width:10px;height:10px}
.panel-features{left:406px;top:60px;width:320px}
.feature{position:absolute;left:0;width:320px;display:flex;gap:14px}
.feature .icon{flex:0 0 36px;width:36px;height:36px}
.feature h3{font-family:"Poppins",Arial,sans-serif;font-weight:600;color:var(--teal);font-size:12px;line-height:1.2}
.feature p{font-size:8.8px;line-height:1.6;margin-top:4px;width:240px}
.panel-idea{left:767px;top:332px;width:300px}
.panel-idea .body{margin-top:22px;font-size:10.2px;line-height:1.6;width:270px}
</style>
</head>
<body>

<!-- Außenseite -->
<section class="spread spread--outside">
  <svg class="shape" style="left:-60px;top:-30px;width:560px;height:680px" viewBox="0 0 100 100" preserveAspectRatio="none"><path d="M40 2 C70 0 98 18 96 48 C94 74 70 94 42 98 C16 100 0 80 2 50 C4 22 14 4 40 2Z" fill="var(--tint)"/></svg>
  <svg class="shape" style="left:560px;top:360px;width:300px;height:430px" viewBox="0 0 100 100" preserveAspectRatio="none"><path d="M50 4 C82 6 98 34 94 62 C90 88 70 102 40 98 C14 94 0 72 6 44 C12 18 26 2 50 4Z" fill="var(--tint)"/></svg>
  <svg class="shape" style="left:860px;top:-40px;width:300px;height:260px" viewBox="0 0 100 100" preserveAspectRatio="none"><path d="M30 4 C60 -4 100 6 98 40 C96 76 70 98 40 90 C14 84 0 60 4 36 C6 20 14 8 30 4Z" fill="var(--lavender)"/></svg>

  <div class="abs panel-why">
    <h2>Warum der 3D-Druck</h2>
    <div class="sub">für mich (und dich?) das einzig Wahre ist</div>
    <svg class="wave" viewBox="0 0 34 8"><path d="M1 5 Q5 1 9 5 T17 5 T25 5 T33 5" fill="none" stroke="var(--teal)" stroke-width="1.6"/></svg>
    <div class="body">
      <p>Ich brenne für neue technische Entwicklungen, die in der Zukunft unser Leben beeinflussen werden. Sei es das autonome Fahren, Kryptowährungen oder der Fortschritt in der Roboterentwicklung. Jedoch hat der 3D-Druck mich vor allem mit seiner Vielfalt und mit den fast grenzenlosen Möglichkeiten in den Bann gezogen. Er gibt mir die Möglichkeit, selbst zum Producer zu werden und eigene individuelle Produkte herzustellen.</p>
      <p>Durch die ausgesprochene Flexibilität in den Anwendungsgebieten kann man immer wieder neue Ideen kreieren und mit wenigen Handgriffen sofort umsetzen. So wie der 3D-Druck sich in den letzten Jahren enorm entwickelt hat, so rasant wächst auch die offene und hilfsbereite Community. Hier ist man unter Gleichgesinnten und Menschen, die das Potenzial dieser neuen und atemberaubenden Technologie erkennen wollen und erkannt haben.</p>
      <p>Die für mich großartigste Errungenschaft des 3D-Druckes ist die <b>Freiheit</b>, eigene Dinge zu entwerfen und <b>sofort zu realisieren</b>. Das Wissen, welches du für diese Freiheit benötigst, möchte ich dir auf dieser Webseite vermitteln. Ich werde den 3D-Druck in allen Bereichen näher für dich beleuchten, sodass du mit den hier gesammelten Erkenntnissen den 3D-Druck entsprechend deinen eigenen Vorstellungen umfangreich nutzen kannst.</p>
    </div>
  </div>

  <svg class="shape" style="left:0;top:600px;width:345px;height:184px" viewBox="0 0 100 100" preserveAspectRatio="none" role="img" aria-label="Foto: Laptop mit 3D-Modell auf dem Bildschirm und gedrucktes Bauteil">
    <defs><linearGradient id="gLaptop" x1="0" y1="0" x2="1" y2="1"><stop offset="0" stop-color="#9aa3ab"/><stop offset="1" stop-color="#2f3a44"/></linearGradient></defs>
    <path d="M0 55 C20 30 50 8 80 4 C96 2 102 20 100 40 L100 100 L0 100Z" fill="url(#gLaptop)"/>
  </svg>

  <div class="abs panel-contact center">
    <h2>Fragen?<br>Kontaktiere uns jetzt!</h2>
    <svg class="wave" viewBox="0 0 34 8"><path d="M1 5 Q5 1 9 5 T17 5 T25 5 T33 5" fill="none" stroke="var(--teal)" stroke-width="1.6"/></svg>
    <p class="intro">Du möchtest mich kennenlernen, wünscht ein Angebot<br>oder hast ein Frage?</p>
    <div class="contact">
      <strong>Angaben gemäß § 5 TMG</strong>
      Jonas Brenner Lindenweg 12 01239 Talstadt<br><br>
      Telefon: 0151 23456789<br>
      E-Mail: <a>kontakt@formwerkstatt-plus.de</a><br>
      <a>www.formwerkstatt-plus.de</a>
    </div>
  </div>

  <svg class="shape" style="left:442px;top:403px;width:200px;height:300px" viewBox="0 0 100 100" preserveAspectRatio="none" role="img" aria-label="Foto: übereinander gelegte Hände als Zeichen von Teamgeist">
    <defs><linearGradient id="gHands" x1="0" y1="0" x2="1" y2="1"><stop offset="0" stop-color="#8a6a58"/><stop offset="1" stop-color="#2b3440"/></linearGradient></defs>
    <path d="M40 2 C66 0 80 18 86 40 C94 62 100 86 78 96 C54 106 20 98 8 76 C-4 52 4 24 18 10 C24 4 32 2 40 2Z" fill="url(#gHands)"/>
  </svg>
  <svg class="shape" style="left:586px;top:414px;width:60px;height:60px" viewBox="0 0 60 60"><circle cx="30" cy="30" r="30" fill="var(--teal)"/></svg>

  <svg class="shape" style="left:732px;top:40px;width:325px;height:405px" viewBox="0 0 100 100" preserveAspectRatio="none" role="img" aria-label="Foto: junger Mann arbeitet konzentriert an einem 3D-Drucker">
    <defs><linearGradient id="gMaker" x1="0" y1="0" x2="1" y2="1"><stop offset="0" stop-color="#4d6372"/><stop offset="1" stop-color="#121c25"/></linearGradient></defs>
    <path d="M60 2 C86 2 100 22 96 44 C92 64 70 70 58 84 C46 98 24 102 10 88 C-2 74 2 50 8 34 C16 12 36 2 60 2Z" fill="url(#gMaker)"/>
  </svg>

  <div class="abs panel-cover center">
    <h2>Kreativität Braucht Mut</h2>
    <svg class="wave" viewBox="0 0 34 8"><path d="M1 5 Q5 1 9 5 T17 5 T25 5 T33 5" fill="none" stroke="var(--teal)" stroke-width="1.6"/></svg>
    <p class="lead">Nutze die Color Fusion Technologie von Printwerk, um deine<br>Produkte zu etwas besonderen zu machen.</p>
    <p class="cta">Lass deine Ideen lebendig werden!</p>
    <div class="brand"><span>formwerkstatt</span><i></i></div>
  </div>
</section>

<!-- Innenseite -->
<section class="spread spread--inside">
  <svg class="shape" style="left:330px;top:300px;width:520px;height:500px" viewBox="0 0 100 100" preserveAspectRatio="none"><path d="M30 6 C56 -2 90 10 96 40 C102 70 84 100 50 100 L0 100 L2 50 C4 28 12 12 30 6Z" fill="var(--tint)"/></svg>
  <svg class="shape" style="left:760px;top:230px;width:380px;height:470px" viewBox="0 0 100 100" preserveAspectRatio="none"><path d="M36 4 C70 -2 100 14 100 40 L100 100 L20 96 C4 84 0 60 6 38 C10 20 20 8 36 4Z" fill="var(--tint)"/></svg>

  <svg class="shape" style="left:0;top:0;width:360px;height:325px" viewBox="0 0 100 100" preserveAspectRatio="none" role="img" aria-label="Foto: Hand hält ein vollfarbig gedrucktes Molekülmodell">
    <defs><linearGradient id="gMolecule" x1="0" y1="0" x2="1" y2="1"><stop offset="0" stop-color="#c98a4a"/><stop offset="0.5" stop-color="#8a6a9a"/><stop offset="1" stop-color="#5b4b7d"/></linearGradient></defs>
    <path d="M0 0 L96 0 C102 20 100 50 88 76 C78 98 56 100 36 84 C22 74 10 76 0 84Z" fill="url(#gMolecule)"/>
  </svg>

  <div class="abs panel-process">
    <h2>Das Verfahren</h2>
    <svg class="wave" viewBox="0 0 34 8"><path d="M1 5 Q5 1 9 5 T17 5 T25 5 T33 5" fill="none" stroke="var(--teal)" stroke-width="1.6"/></svg>
    <div class="body">
      <p>Das Color Fusion Verfahren ist nicht nur sehr schnell, sondern brilliert auch mit einer hervorragenden Bauteilqualität, da die 3D-Drucker eine Auflösung von 1200 dpi aufweisen. Mit dieser hohen Auflösung stellen auch kleinste Details keine Probleme dar, sodass auch bis zu Gewinde M5 gedruckt werden können. Die Pulver Wiederverwendbarkeit bei dem Printwerk Color Fusion 580 3D-Drucker liegt bei 80%.</p>
      <p>Die gedruckten Teile müssen im Nachgang noch entpulvert werden und können dann auch weiter bearbeitet werden (Fräsen, Bohren, Färben, infiltrieren, etc.).</p>
    </div>
    <div class="uses-title">Anwendungsgebiete:</div>
    <ul class="uses">
      <li><svg viewBox="0 0 10 10"><circle cx="5" cy="5" r="5" fill="var(--teal)"/><path d="M2.6 5.2 L4.3 6.8 L7.4 3.5" fill="none" stroke="#fff" stroke-width="1.2"/></svg>Prototypen</li>
      <li><svg viewBox="0 0 10 10"><circle cx="5" cy="5" r="5" fill="var(--teal)"/><path d="M2.6 5.2 L4.3 6.8 L7.4 3.5" fill="none" stroke="#fff" stroke-width="1.2"/></svg>Prothesen</li>
      <li><svg viewBox="0 0 10 10"><circle cx="5" cy="5" r="5" fill="var(--teal)"/><path d="M2.6 5.2 L4.3 6.8 L7.4 3.5" fill="none" stroke="#fff" stroke-width="1.2"/></svg>Spielzeug</li>
      <li><svg viewBox="0 0 10 10"><circle cx="5" cy="5" r="5" fill="var(--teal)"/><path d="M2.6 5.2 L4.3 6.8 L7.4 3.5" fill="none" stroke="#fff" stroke-width="1.2"/></svg>Kleinserien</li>
      <li><svg viewBox="0 0 10 10"><circle cx="5" cy="5" r="5" fill="var(--teal)"/><path d="M2.6 5.2 L4.3 6.8 L7.4 3.5" fill="none" stroke="#fff" stroke-width="1.2"/></svg>Funktionsmodelle</li>
      <li><svg viewBox="0 0 10 10"><circle cx="5" cy="5" r="5" fill="var(--teal)"/><path d="M2.6 5.2 L4.3 6.8 L7.4 3.5" fill="none" stroke="#fff" stroke-width="1.2"/></svg>Architekturmodelle</li>
      <li><svg viewBox="0 0 10 10"><circle cx="5" cy="5" r="5" fill="var(--teal)"/><path d="M2.6 5.2 L4.3 6.8 L7.4 3.5" fill="none" stroke="#fff" stroke-width="1.2"/></svg>Modellbau</li>
      <li><svg viewBox="0 0 10 10"><circle cx="5" cy="5" r="5" fill="var(--teal)"/><path d="M2.6 5.2 L4.3 6.8 L7.4 3.5" fill="none" stroke="#fff" stroke-width="1.2"/></svg>Präsentationen</li>
      <li><svg viewBox="0 0 10 10"><circle cx="5" cy="5" r="5" fill="var(--teal)"/><path d="M2.6 5.2 L4.3 6.8 L7.4 3.5" fill="none" stroke="#fff" stroke-width="1.2"/></svg>Beschriftungen</li>
      <li><svg viewBox="0 0 10 10"><circle cx="5" cy="5" r="5" fill="var(--teal)"/><path d="M2.6 5.2 L4.3 6.8 L7.4 3.5" fill="none" stroke="#fff" stroke-width="1.2"/></svg>uvm.</li>
    </ul>
  </div>

  <svg class="shape" style="left:161px;top:615px;width:200px;height:160px" viewBox="0 0 100 100" preserveAspectRatio="none" role="img" aria-label="Gedrucktes weißes Architekturmodell eines Hauses">
    <defs><linearGradient id="gHouse" x1="0" y1="0" x2="1" y2="1"><stop offset="0" stop-color="#f1f1f1"/><stop offset="1" stop-color="#cfcfcf"/></linearGradient></defs>
    <path d="M10 30 L60 8 L98 24 L98 96 L10 96Z" fill="url(#gHouse)"/>
  </svg>

  <div class="abs panel-features">
    <h2>Produktion von Bauteilen<br>in Vollfarbe</h2>
    <svg class="wave" viewBox="0 0 34 8"><path d="M1 5 Q5 1 9 5 T17 5 T25 5 T33 5" fill="none" stroke="var(--teal)" stroke-width="1.6"/></svg>

    <div class="feature" style="top:98px">
      <svg class="icon" viewBox="0 0 36 36"><circle cx="18" cy="18" r="18" fill="var(--teal)"/><circle cx="18" cy="18" r="14.5" fill="none" stroke="#fff" stroke-width="1"/><circle cx="18" cy="19" r="7" fill="none" stroke="#fff" stroke-width="1.5"/><path d="M18 15 V19 L21 21 M16 10.5 H20" fill="none" stroke="#fff" stroke-width="1.5"/></svg>
      <div><h3>Schnelle Produktion von<br>Prototypen</h3><p>Erstellen von mehreren Prototypen in derselben Zeit, die für den Druck eines einzelnen Teils beansprucht wird.</p></div>
    </div>
    <div class="feature" style="top:202px">
      <svg class="icon" viewBox="0 0 36 36"><circle cx="18" cy="18" r="18" fill="var(--teal)"/><circle cx="18" cy="18" r="14.5" fill="none" stroke="#fff" stroke-width="1"/><path d="M10 25 L25 10 L25 25Z M14 25 V23 M18 25 V22 M22 25 V23" fill="none" stroke="#fff" stroke-width="1.5"/></svg>
      <div><h3>Exakte, funktionale, Detailreiche<br>Bauteile</h3><p>Ultradünne Schichten von 80 Mikron (0,08 mm) und einer Auflösung von 1.200 dpi in der X-Y-Achse.</p></div>
    </div>
    <div class="feature" style="top:296px">
      <svg class="icon" viewBox="0 0 36 36"><circle cx="18" cy="18" r="18" fill="var(--teal)"/><circle cx="18" cy="18" r="14.5" fill="none" stroke="#fff" stroke-width="1"/><path d="M24 10 L16 19 M15 20 C12 20 11 23 10 26 C13 25 16 24 16 21Z" fill="none" stroke="#fff" stroke-width="1.5"/></svg>
      <div><h3>Vollfarbdruck auf Voxelebene</h3><p>Vollfarbige Funktionsteile in brillanten Farben ohne Beeinträchtigung der mechanischen Eigenschaften.</p></div>
    </div>
    <div class="feature" style="top:376px">
      <svg class="icon" viewBox="0 0 36 36"><circle cx="18" cy="18" r="18" fill="var(--teal)"/><circle cx="18" cy="18" r="14.5" fill="none" stroke="#fff" stroke-width="1"/><rect x="11" y="11" width="14" height="14" fill="none" stroke="#fff" stroke-width="1.5"/><path d="M11 18 H25 M18 11 V25" stroke="#fff" stroke-width="1.2"/></svg>
      <div><h3>Hohe Bauteildichte</h3><p>Technische Teile aus thermoplastischem Kunststoff mit optimalen mechanischen Eigenschaften</p></div>
    </div>
    <div class="feature" style="top:456px">
      <svg class="icon" viewBox="0 0 36 36"><circle cx="18" cy="18" r="18" fill="var(--teal)"/><circle cx="18" cy="18" r="14.5" fill="none" stroke="#fff" stroke-width="1"/><path d="M18 26 C10 24 9 16 11 11 C17 12 20 17 18 26Z M18 26 C26 24 27 16 25 11 C19 12 16 17 18 26Z" fill="none" stroke="#fff" stroke-width="1.4"/></svg>
      <div><h3>Bioverträgliches Material</h3><p>Pulver und Agents werden als ungefährlich eingestuft, daher gibt es eine Vielzahl von Anwendungsmöglichkeiten.</p></div>
    </div>
  </div>

  <svg class="shape" style="left:384px;top:610px;width:316px;height:145px" viewBox="0 0 100 100" preserveAspectRatio="none" role="img" aria-label="Vollfarbig gedruckter Clownfisch">
    <defs><linearGradient id="gFish" x1="0" y1="0" x2="1" y2="0"><stop offset="0" stop-color="#e4532f"/><stop offset="0.5" stop-color="#f08a5d"/><stop offset="1" stop-color="#d9402a"/></linearGradient></defs>
    <path d="M4 50 C16 30 30 40 40 30 C54 10 78 14 92 34 C100 48 98 66 88 76 C72 92 50 92 36 72 C28 64 16 76 4 70 Z" fill="url(#gFish)"/>
  </svg>

  <svg class="shape" style="left:800px;top:0;width:300px;height:292px" viewBox="0 0 100 100" preserveAspectRatio="none" role="img" aria-label="Vollfarbig gedruckte Gitterkugel in Rot, Grün und Blau">
    <defs><radialGradient id="gLattice" cx="0.45" cy="0.45" r="0.6"><stop offset="0" stop-color="#5a6fb0"/><stop offset="0.55" stop-color="#4f8a3e"/><stop offset="1" stop-color="#d2354d"/></radialGradient></defs>
    <path d="M10 0 L100 0 L100 86 C86 98 60 102 38 92 C14 80 0 56 2 32 C3 18 6 8 10 0Z" fill="url(#gLattice)"/>
  </svg>

  <div class="abs panel-idea">
    <h2>Deine Idee in Vollfarbe<br>drucken!</h2>
    <svg class="wave" viewBox="0 0 34 8"><path d="M1 5 Q5 1 9 5 T17 5 T25 5 T33 5" fill="none" stroke="var(--teal)" stroke-width="1.6"/></svg>
    <div class="body">
      <p>Du möchtest gern deine Idee in Vollfarbe gedruckt haben? Dann bist du hier richtig!</p>
      <p>Egal ob Hobbybastler, Student oder Firma, gemeinsam werden wir dein Modell realisieren.</p>
      <p>Jetzt einfach Kontakt aufnehmen<br>und dir dein unverbindliches<br>Angebot einholen!</p>
    </div>
  </div>

  <svg class="shape" style="left:870px;top:570px;width:230px;height:214px" viewBox="0 0 100 100" preserveAspectRatio="none" role="img" aria-label="Vollfarbig gedruckte Spiralfigur in Regenbogenfarben">
    <defs><linearGradient id="gSpiral" x1="0" y1="1" x2="1" y2="0"><stop offset="0" stop-color="#e94a6a"/><stop offset="0.35" stop-color="#f2c14a"/><stop offset="0.65" stop-color="#5cb85c"/><stop offset="1" stop-color="#5a5fb8"/></linearGradient></defs>
    <path d="M30 0 C48 0 54 18 50 34 C62 40 80 44 100 50 L100 100 L0 100 C0 80 10 62 26 56 C20 40 14 20 18 10 C20 4 24 0 30 0Z" fill="url(#gSpiral)"/>
  </svg>
</section>

</body>
</html>
```